Stationary, memo and report templates for professional services company

Looking for someone to update stationary design but just as importantly come up with a template for reports and memos for use in our consulting firm. Would also like some brand use guidelines to be able to share with our whole team. We have an existing logo that we like. Need to update with a more contemporary look so that our deliverables to clients look good and professional yet stylish. This is for business to business communications. No need for envelope design. Important to have design for multiple pages, i.e. first page of a report and then 2nd page. Need to use in MS word documents so must be easy to use and replicate. Don't want something overly complex. Clean, fresh looking is best.

Target Market(s)

Business to business; non-profit cultural attractions

Colors

Designer to choose colors to be used in the design.

Requirements
Must have
• Clean look but with a little style or pop. Something that can easily be used in word documents. Need to have page styles that have a first page of a report (not a cover page) and then secondary page.
Nice to have
• Although the dark blue is our primary color. Might be willing to look at some accent color as well.
Should not have
• Not just our logo on the page with a color bar.

```html
<!DOCTYPE html>
<html lang="en">
<head>
<meta charset="utf-8">
<title>Halden Advisors – Stationery, Memo and Report Templates</title>
<link href="https://fonts.googleapis.com/css2?family=Libre+Franklin:wght@400;600;700;800&family=Questrial&family=Open+Sans:wght@400;600;700&display=swap" rel="stylesheet">
<style>
:root{
  --backdrop:#e3e3e3;
  --paper:#ffffff;
  --brand:#1a4f9c;
  --brand-deep:#0d2f78;
  --brand-bright:#2263b8;
  --ink:#3a3a3a;
  --ink-soft:#8a8a8a;
  --rule:#c9c9c9;
  --white:#ffffff;
}
*{box-sizing:border-box;margin:0;padding:0}
html,body{width:1200px;height:1085px;overflow:hidden;background:var(--backdrop)}
body{position:relative;font-family:"Open Sans",Arial,sans-serif;color:var(--ink)}
.page{position:absolute;width:330px;height:467px;background:var(--paper);box-shadow:0 1px 4px rgba(0,0,0,.25);overflow:hidden}
.col-1{left:77px}.col-2{left:433px}.col-3{left:791px}
.row-1{top:62px}.row-2{top:556px}
.page-foot{position:absolute;left:0;right:0;bottom:0;height:8px;border-top:1px solid var(--rule)}
.page-foot::after{content:"";position:absolute;left:0;right:0;bottom:0;height:5px;background:linear-gradient(90deg,var(--brand-deep),var(--brand-bright) 60%,var(--brand-deep))}

.wordmark{font-family:"Libre Franklin",Arial,sans-serif;font-weight:600;color:var(--brand);line-height:1.05;letter-spacing:.02em}
.wordmark.small{position:absolute;left:26px;top:30px;font-size:10px}
.wordmark.tiny{font-size:8px;text-align:right}

.contact-block{position:absolute;right:26px;top:30px;width:84px;border-left:1px solid var(--rule);padding-left:6px;font-family:"Questrial",sans-serif;font-size:4.6px;line-height:1.55;color:var(--ink-soft)}
.contact-block li{list-style:none;display:flex;align-items:center;gap:2px}
.contact-block svg{width:4px;height:4px;fill:var(--brand)}

/* letter */
.letter-body{position:absolute;left:26px;top:110px;width:278px;font-family:"Questrial",sans-serif;font-size:4.8px;line-height:1.6;color:var(--ink-soft)}
.letter-body .salutation{font-size:8px;color:var(--ink);margin-bottom:12px}
.letter-body p{margin-bottom:7px}
.signature{font-family:"Questrial",sans-serif;font-style:normal;font-size:11px;color:var(--brand);margin-top:8px}

/* memo */
.memo-title{position:absolute;left:26px;top:148px;font-family:"Libre Franklin",sans-serif;font-weight:700;font-size:9px;color:var(--brand)}
.memo-fields{position:absolute;left:26px;top:168px;width:278px;font-family:"Questrial",sans-serif;font-size:6px;color:var(--ink)}
.memo-line{display:flex;align-items:flex-end;gap:3px;height:20px}
.memo-line .fill{flex:1;border-bottom:1px solid var(--ink-soft);margin-bottom:2px}
.memo-line .fill.short{flex:0 0 72px}

/* cover */
.cover-mark{position:absolute;left:0;right:0;top:180px;text-align:center;font-family:"Libre Franklin",sans-serif;font-weight:600;font-size:40px;line-height:1;color:var(--brand);letter-spacing:.02em}
.cover-mark span{display:block;font-size:26px;margin-top:6px}
.report-name{position:absolute;left:26px;top:374px;font-family:"Libre Franklin",sans-serif;font-weight:800;font-size:34px;color:var(--brand-deep);letter-spacing:.01em}
.report-intro{position:absolute;left:26px;top:416px;width:280px;font-size:4.9px;line-height:1.45;color:var(--ink)}

/* contents */
.section-head{position:absolute;left:26px;top:28px;right:26px;border-bottom:1px solid var(--brand);padding-bottom:3px}
.section-head h2{font-family:"Libre Franklin",sans-serif;font-weight:700;font-size:15px;color:var(--brand-deep);line-height:1.05}
.section-head p{font-family:"Libre Franklin",sans-serif;font-size:10.5px;color:var(--ink)}
.section-head .wordmark{position:absolute;right:0;top:2px}
.toc{position:absolute;left:26px;right:26px;top:76px;list-style:none}
.toc li{height:48px}
.toc-title{display:flex;align-items:flex-end;font-family:"Open Sans",sans-serif;font-weight:700;font-size:6px;color:var(--brand)}
.toc-title .leader{flex:0 0 118px;border-bottom:1px solid var(--brand);margin:0 1px 2px}
.toc li p{font-size:4.4px;line-height:1.5;color:var(--ink);margin-top:6px}

.features{position:absolute;left:26px;right:26px;top:82px}
.feature{display:flex;gap:8px;height:122px}
.feature .photo{flex:0 0 104px;height:104px;border-radius:6px}
.feature h3{font-family:"Open Sans",sans-serif;font-weight:700;font-size:6px;color:var(--brand-deep);margin-bottom:3px}
.feature p{font-size:5.2px;line-height:1.45;color:var(--ink);margin-bottom:5px}
.photo-office{background:linear-gradient(135deg,#c9d3dc,#6f8398)}
.photo-portrait{background:linear-gradient(135deg,#a9b7c2,#2f3a48)}
.photo-team{background:linear-gradient(135deg,#cbbfb2,#8a6f5c)}

/* back cover */
.back{background:linear-gradient(180deg,var(--brand-bright),var(--brand-deep))}
.back .cover-mark{color:var(--white);top:184px}
.back-contact{position:absolute;left:0;right:0;top:405px;text-align:center;color:var(--white);font-size:4.6px;line-height:1.5}
.back-contact h4{display:flex;align-items:center;justify-content:center;gap:8px;font-size:7px;font-weight:700;margin-bottom:3px}
.back-contact h4::before,.back-contact h4::after{content:"";width:48px;border-top:1px solid var(--white)}
</style>
</head>
<body>

<svg width="0" height="0" style="position:absolute">
  <symbol id="icon-phone" viewBox="0 0 10 10"><circle cx="5" cy="5" r="5"/></symbol>
</svg>

<!-- Letterhead -->
<section class="page col-1 row-1" aria-label="Letterhead">
  <div class="wordmark small">Halden<br>Advisors</div>
  <ul class="contact-block">
    <li>412 Larchwood Drive</li>
    <li>Fairview, Oregon 97024</li>
    <li><svg><use href="#icon-phone"/></svg>(555) 201-0188</li>
    <li><svg><use href="#icon-phone"/></svg>mark@haldenadvisors.com</li>
    <li><svg><use href="#icon-phone"/></svg>www.haldenadvisors.com</li>
  </ul>
  <div class="letter-body">
    <p class="salutation">Dear Mr. Ellis,</p>
    <p>Thank you for meeting with our team last week. We have reviewed your goals and prepared a plan that covers scope, timing and budget for the coming season.</p>
    <p>Our approach begins with a short discovery phase, followed by workshops with your staff and a clear set of recommendations for visitor growth.</p>
    <p>We will share progress reports each month and remain available for calls whenever questions arise during the project.</p>
    <p>Please review the attached proposal and let us know if any changes are needed.</p>
    <p>Sincerely,</p>
    <p class="signature">Mark Ellis</p>
  </div>
  <div class="page-foot"></div>
</section>

<!-- Memo -->
<section class="page col-2 row-1" aria-label="Memo">
  <div class="wordmark small">Halden<br>Advisors</div>
  <ul class="contact-block">
    <li>412 Larchwood Drive</li>
    <li>Fairview, Oregon 97024</li>
    <li><svg><use href="#icon-phone"/></svg>(555) 201-0188</li>
    <li><svg><use href="#icon-phone"/></svg>mark@haldenadvisors.com</li>
    <li><svg><use href="#icon-phone"/></svg>www.haldenadvisors.com</li>
  </ul>
  <h1 class="memo-title">MEMO</h1>
  <div class="memo-fields">
    <div class="memo-line">To :<span class="fill"></span>Date :<span class="fill short"></span></div>
    <div class="memo-line">From :<span class="fill"></span></div>
    <div class="memo-line">Subject :<span class="fill"></span></div>
  </div>
  <div class="page-foot"></div>
</section>

<!-- Report cover -->
<section class="page col-3 row-1" aria-label="Report first page">
  <div class="cover-mark">Halden<span>Advisors</span></div>
  <h1 class="report-name">REPORT NAME</h1>
  <p class="report-intro">Lorem ipsum dolor sit amet, consectetur adipiscing elit. Haec para/doca illi, nos admirabilia dicamus. Unum igitur tibi litteram videor an totas paginas commovere? Idem etiam dolorem saepe perpetuntur, ne, si id non facient, incidant in maiorem. Si enim ad populum me vocas, eum. Virtutem est enim in dividendo partem in genere numerare.</p>
  <div class="page-foot"></div>
</section>

<!-- Contents, text version -->
<section class="page col-1 row-2" aria-label="Table of contents">
  <header class="section-head">
    <h2>Table of Contents</h2>
    <p>Your Text Here</p>
    <div class="wordmark tiny">Halden<br>Advisors</div>
  </header>
  <ol class="toc">
    <li><div class="toc-title">LOREM IPSUM<span class="leader"></span>1</div><p>Brief summary of this section with key findings, supporting data and next steps for the team.</p></li>
    <li><div class="toc-title">LOREM IPSUM<span class="leader"></span>2</div><p>Brief summary of this section with key findings, supporting data and next steps for the team.</p></li>
    <li><div class="toc-title">LOREM IPSUM<span class="leader"></span>3</div><p>Brief summary of this section with key findings, supporting data and next steps for the team.</p></li>
    <li><div class="toc-title">LOREM IPSUM<span class="leader"></span>4</div><p>Brief summary of this section with key findings, supporting data and next steps for the team.</p></li>
    <li><div class="toc-title">LOREM IPSUM<span class="leader"></span>5</div><p>Brief summary of this section with key findings, supporting data and next steps for the team.</p></li>
    <li><div class="toc-title">LOREM IPSUM<span class="leader"></span>6</div><p>Brief summary of this section with key findings, supporting data and next steps for the team.</p></li>
    <li><div class="toc-title">LOREM IPSUM<span class="leader"></span>7</div><p>Brief summary of this section with key findings, supporting data and next steps for the team.</p></li>
    <li><div class="toc-title">LOREM IPSUM<span class="leader"></span>8</div><p>Brief summary of this section with key findings, supporting data and next steps for the team.</p></li>
  </ol>
  <div class="page-foot"></div>
</section>

<!-- Contents, feature version -->
<section class="page col-2 row-2" aria-label="Secondary report page">
  <header class="section-head">
    <h2>Table of Contents</h2>
    <p>Your Text Here</p>
    <div class="wordmark tiny">Halden<br>Advisors</div>
  </header>
  <div class="features">
    <article class="feature">
      <div class="photo photo-office" role="img" aria-label="Photo of a consultant at an office desk"></div>
      <div>
        <h3>LOREM IPSUM DOLOR SIT AMET</h3>
        <p>Lorem ipsum dolor sit amet, consectetur adipiscing elit. Contemnit enim disserendi elegantiam, confuse loquitur. Cur post Tarentum ad Archytam? Quem Tiberina descensio festo illo die tanto gaudio affecit, quanto L. Tibi hoc incredibile, quod beatissimum.</p>
        <p>Is ita vivebat, ut nulla tam exquisita posset inveniri voluptas, qua non abundaret. Expectoque quid ad id, quod quaerebam, respondeas.</p>
      </div>
    </article>
    <article class="feature">
      <div class="photo photo-portrait" role="img" aria-label="Portrait photo of a business professional"></div>
      <div>
        <h3>CONSECTETUR ADIPISCING ELIT</h3>
        <p>Lorem ipsum dolor sit amet, consectetur adipiscing elit. Contemnit enim disserendi elegantiam, confuse loquitur. Cur post Tarentum ad Archytam? Quem Tiberina descensio festo illo die tanto gaudio affecit, quanto L. Tibi hoc incredibile, quod beatissimum.</p>
        <p>Is ita vivebat, ut nulla tam exquisita posset inveniri voluptas, qua non abundaret. Expectoque quid ad id, quod quaerebam, respondeas.</p>
      </div>
    </article>
    <article class="feature">
      <div class="photo photo-team" role="img" aria-label="Photo of two colleagues working together"></div>
      <div>
        <h3>PROCLIVI CURRIT ORATIO</h3>
        <p>Lorem ipsum dolor sit amet, consectetur adipiscing elit. Contemnit enim disserendi elegantiam, confuse loquitur. Cur post Tarentum ad Archytam? Quem Tiberina descensio festo illo die tanto gaudio affecit, quanto L. Tibi hoc incredibile, quod beatissimum.</p>
        <p>Is ita vivebat, ut nulla tam exquisita posset inveniri voluptas, qua non abundaret. Expectoque quid ad id, quod quaerebam, respondeas.</p>
      </div>
    </article>
  </div>
  <div class="page-foot"></div>
</section>

<!-- Back cover -->
<section class="page col-3 row-2 back" aria-label="Back cover">
  <div class="cover-mark">Halden<span>Advisors</span></div>
  <div class="back-contact">
    <h4>CONTACT US</h4>
    <p>412 Larchwood Drive, Fairview, Oregon 97024</p>
    <p>Phone : (555) 201-0188 Email : mark@haldenadvisors.com</p>
    <p>Web : www.haldenadvisors.com</p>
  </div>
</section>

</body>
</html>
```